Pediatric Dental Practice needs a postcard for direct mail advertising

We are looking for a creative and professional double-sided postcard design for a direct mail marketing campaign. Our goal is to attract new families to our pediatric dental practice by conveying a sense of warmth, modern care, and clinical excellence. The design should feel "boutique" and high-end yet remain fun and approachable for parents and children.

```html
<!DOCTYPE html>
<html lang="en">
<head>
<meta charset="utf-8">
<title>Brightleaf Pediatric Dentistry – Postcard</title>
<link href="https://fonts.googleapis.com/css2?family=Libre+Franklin:wght@400;500;600;800;900&display=swap" rel="stylesheet">
<style>
:root{
  --stage:#2d2d2d;
  --mint:#d8e8d8;
  --mint-pale:#e6f0e6;
  --mint-deep:#d3e6d3;
  --green:#2f9e52;
  --green-dark:#1f6b3c;
  --green-band:#5fbf74;
  --ink:#1f1f1f;
  --ink-soft:#2b2b2b;
  --white:#ffffff;
  --line:#3a3a3a;
}
*{margin:0;padding:0;box-sizing:border-box}
html,body{width:894px;height:1200px;overflow:hidden;background:var(--stage);font-family:"Libre Franklin",Arial,sans-serif;color:var(--ink)}
.card{position:absolute;left:73px;width:749px;height:499px;overflow:hidden}
.card--front{top:70px;background:var(--white)}
.card--back{top:619px;background:var(--mint-pale)}

/* front */
.front-panel{position:absolute;left:0;top:0;width:381px;height:499px;background:var(--mint);border-radius:0 34px 34px 0}
.brand{position:absolute;left:24px;top:74px;width:170px;text-align:center}
.brand__dot{display:block;width:34px;height:34px;border-radius:50%;background:var(--green-band);margin:0 auto 10px}
.brand__name{font-size:26px;font-weight:500;color:var(--ink-soft);line-height:1;letter-spacing:.3px}
.brand__tag{font-size:9px;font-weight:500;letter-spacing:3.2px;color:var(--ink-soft);margin-top:6px;white-space:nowrap}
.clinic-photo{position:absolute;left:220px;top:23px;width:216px;height:115px;border-radius:12px;background:linear-gradient(135deg,#e9e2cf 0%,#d7dccb 45%,#7fbfb8 80%,#5aa2ad 100%)}
.headline{position:absolute;left:22px;top:163px;font-size:23.5px;font-weight:900;line-height:27px;color:var(--ink-soft);letter-spacing:-.2px;white-space:nowrap}
.headline em{font-style:normal;color:var(--green)}
.intro{position:absolute;left:23px;top:228px;width:340px;font-size:12.4px;line-height:17px;color:var(--ink-soft)}
.perks{position:absolute;left:23px;top:284px;width:330px;display:grid;grid-template-columns:154px 155px;column-gap:16px;row-gap:11px;list-style:none}
.perk{height:32px;background:var(--white);border-radius:16px;display:flex;align-items:center;font-size:10.4px;color:var(--ink);position:relative;padding-left:31px}
.perk::before{content:"";position:absolute;left:0;top:4px;width:24px;height:24px;border-radius:50%;background:#9ed3a8}
.contact-front{position:absolute;left:25px;top:425px}
.contact-front .phone{display:flex;align-items:center;gap:10px;font-size:20.5px;font-weight:800;color:var(--green)}
.contact-front .web{display:flex;align-items:center;gap:12px;font-size:15.5px;color:var(--green);margin-top:10px}
.stamp{position:absolute;left:665px;top:17px;width:64px;height:75px;border:1.5px solid #9bb5a0;border-radius:3px;display:flex;align-items:center;justify-content:center;text-align:center;font-size:8.5px;font-weight:600;letter-spacing:.6px;line-height:13px;color:var(--ink-soft)}
.address-label{position:absolute;left:419px;top:262px;font-size:15px;color:var(--ink-soft)}
.address-line{position:absolute;left:421px;width:292px;height:1px;background:var(--line)}

/* back */
.back-curve{position:absolute;left:0;top:0}
.back-title{position:absolute;left:26px;top:24px;font-size:36.5px;font-weight:900;line-height:39.5px;letter-spacing:-.6px;color:#111}
.back-title em{font-style:normal;color:var(--green)}
.back-intro{position:absolute;left:26px;top:161px;width:330px;font-size:16.8px;line-height:23px;color:var(--ink-soft)}
.kids-photo{position:absolute;left:24px;top:241px;width:466px;height:179px;border-radius:90px 90px 0 0;background:linear-gradient(90deg,#b98a6e 0%,#8c5f49 25%,#e6d2a8 52%,#6f8fc0 78%,#d8c7b2 100%);opacity:.85}
.services{position:absolute;left:511px;top:12px;width:215px;list-style:none}
.service{height:67px;display:flex;align-items:center;gap:17px;padding-left:11px;border-bottom:1px solid #a9cdb0}
.service:last-child{border-bottom:none}
.service__icon{width:50px;height:50px;border-radius:50%;background:var(--white);display:flex;align-items:center;justify-content:center;flex:none}
.service__label{font-size:13px;font-weight:600;line-height:18.5px;letter-spacing:.3px;color:var(--green-dark);text-transform:uppercase}
.footer-band{position:absolute;left:0;top:419px;width:749px;height:80px;background:var(--green-band);color:var(--white)}
.welcome{position:absolute;left:25px;top:18px;font-size:18.5px;line-height:25px}
.welcome strong{font-weight:900;display:block}
.band-divider{position:absolute;top:19px;width:1px;height:43px;background:rgba(255,255,255,.7)}
.band-address{position:absolute;left:253px;top:22px;display:flex;gap:16px;align-items:flex-start;font-size:14.3px;line-height:20px}
.band-contact{position:absolute;left:543px;top:17px}
.band-contact .phone{display:flex;align-items:center;gap:8px;font-size:20px;font-weight:800}
.band-contact .web{display:flex;align-items:center;gap:12px;font-size:15.5px;margin-top:5px}
</style>
</head>
<body>

<section class="card card--front" aria-label="Postcard front">
  <div class="front-panel"></div>

  <div class="brand">
    <span class="brand__dot"></span>
    <div class="brand__name">brightleaf</div>
    <div class="brand__tag">PEDIATRIC DENTISTRY</div>
  </div>

  <div class="clinic-photo" role="img" aria-label="Photo of a bright modern pediatric treatment room with a teal dental chair and a window"></div>

  <h1 class="headline">GROWING <em>HEALTHY</em> SMILES.<br>CREATING <em>HAPPY VISITS.</em></h1>
  <p class="intro">Specialized paediatric dental care for infants, children &amp; teens in a calm, modern, family-friendly environment.</p>

  <ul class="perks">
    <li class="perk">Kid-first experience</li>
    <li class="perk">Gentle &amp; expert care</li>
    <li class="perk">Restorative Treatments</li>
    <li class="perk">Orthodontic Evaluations</li>
    <li class="perk">Sedation Options</li>
    <li class="perk">Emergency Dental Care</li>
  </ul>

  <div class="contact-front">
    <div class="phone">
      <svg width="20" height="20" viewBox="0 0 24 24" aria-hidden="true"><path fill="#2f9e52" d="M6.6 10.8a15.1 15.1 0 0 0 6.6 6.6l2.2-2.2a1 1 0 0 1 1-.25 11.4 11.4 0 0 0 3.6.57 1 1 0 0 1 1 1V20a1 1 0 0 1-1 1A17 17 0 0 1 3 4a1 1 0 0 1 1-1h3.5a1 1 0 0 1 1 1c0 1.25.2 2.45.57 3.57a1 1 0 0 1-.25 1z"/></svg>
      (905) 555-0148
    </div>
    <div class="web">
      <svg width="18" height="18" viewBox="0 0 24 24" aria-hidden="true" fill="none" stroke="#2f9e52" stroke-width="2"><circle cx="12" cy="12" r="10" fill="#2f9e52"/><path stroke="#d8e8d8" stroke-width="1.4" d="M2 12h20M12 2c3 3 3 17 0 20M12 2c-3 3-3 17 0 20M4 7h16M4 17h16"/></svg>
      brightleafdentistry.ca
    </div>
  </div>

  <div class="stamp">PLACE<br>STAMP<br>HERE</div>
  <div class="address-label">To</div>
  <div class="address-line" style="top:318px"></div>
  <div class="address-line" style="top:361px"></div>
  <div class="address-line" style="top:402px;left:423px"></div>
  <div class="address-line" style="top:447px"></div>
</section>

<section class="card card--back" aria-label="Postcard back">
  <svg class="back-curve" width="749" height="420" viewBox="0 0 749 420" aria-hidden="true">
    <path d="M400 0 C450 90 470 200 420 420 L749 420 L749 0 Z" fill="var(--mint-deep)"/>
  </svg>

  <h2 class="back-title">Dentistry designed<br><em>for little smiles and<br>big comfort.</em></h2>
  <p class="back-intro">From first visits to orthodontic checkups, we’re here for every stage of your child’s dental journey.</p>

  <div class="kids-photo" role="img" aria-label="Photo of four smiling children lying side by side"></div>

  <ul class="services">
    <li class="service">
      <span class="service__icon"><svg width="28" height="28" viewBox="0 0 24 24" fill="none" stroke="#2f9e52" stroke-width="1.6" stroke-linejoin="round"><path d="M7 4c2 0 3 1 5 1s3-1 5-1c3 0 4 3 3 6-1 2-1 4-2 8-.5 2-2 2-2.5 0L14 14c-.5-1.5-3.5-1.5-4 0l-1.5 4c-.5 2-2 2-2.5 0-1-4-1-6-2-8-1-3 0-6 3-6z"/></svg></span>
      <span class="service__label">Preventive<br>dental care</span>
    </li>
    <li class="service">
      <span class="service__icon"><svg width="28" height="28" viewBox="0 0 24 24" fill="none" stroke="#2f9e52" stroke-width="1.6" stroke-linejoin="round"><rect x="3" y="5" width="18" height="7" rx="2"/><path d="M7 5v7M11 5v7M15 5v7M12 12v4h3l2 4"/></svg></span>
      <span class="service__label">Dental exams &amp;<br>cleanings</span>
    </li>
    <li class="service">
      <span class="service__icon"><svg width="30" height="30" viewBox="0 0 24 24" fill="none" stroke="#2f9e52" stroke-width="1.4" stroke-linejoin="round"><circle cx="12" cy="12" r="10"/><path d="M8.5 7c1.4 0 2.2.6 3.5.6s2.1-.6 3.5-.6c2 0 2.6 2 2 4-.6 1.4-.7 2.7-1.3 5.3-.3 1.3-1.3 1.3-1.6 0L14 14c-.4-1-3.6-1-4 0l-.6 2.3c-.3 1.3-1.3 1.3-1.6 0-.6-2.6-.7-3.9-1.3-5.3-.6-2 0-4 2-4z"/></svg></span>
      <span class="service__label">Restorative<br>treatments</span>
    </li>
    <li class="service">
      <span class="service__icon"><svg width="28" height="28" viewBox="0 0 24 24" fill="none" stroke="#2f9e52" stroke-width="1.6" stroke-linejoin="round"><path d="M7 3c2 0 3 1 5 1s3-1 5-1c3 0 4 3 3 6-1 2-1 4-2 8-.5 2-2 2-2.5 0L14 13c-.5-1.5-3.5-1.5-4 0l-1.5 4c-.5 2-2 2-2.5 0-1-4-1-6-2-8-1-3 0-6 3-6z"/><rect x="9" y="7" width="6" height="3.5" rx=".5"/><path d="M4.5 8.7h4.5M15 8.7h4.5"/></svg></span>
      <span class="service__label">Orthodontic<br>evaluations</span>
    </li>
    <li class="service">
      <span class="service__icon"><svg width="28" height="28" viewBox="0 0 24 24" fill="none" stroke="#2f9e52" stroke-width="1.5" stroke-linecap="round"><path d="M18 3l3 3M19.5 4.5 11 13l-2 2-1 1M9 11l4 4M14 6l4 4M8 16l-2 2"/><path d="M2 13h2l-2 2h2M4 17h2l-2 2h2"/></svg></span>
      <span class="service__label">Sedation<br>options</span>
    </li>
    <li class="service">
      <span class="service__icon"><svg width="28" height="28" viewBox="0 0 24 24" fill="none" stroke="#2f9e52" stroke-width="1.5" stroke-linejoin="round"><rect x="3" y="7" width="16" height="12" rx="2"/><path d="M8 7V5h6v2M11 10v6M8 13h6"/><circle cx="19" cy="17" r="3" fill="#fff"/></svg></span>
      <span class="service__label">Emergency<br>dental care</span>
    </li>
  </ul>

  <div class="footer-band">
    <p class="welcome"><strong>NEW PATIENTS</strong>ALWAYS WELCOME!</p>
    <span class="band-divider" style="left:231px"></span>
    <div class="band-address">
      <svg width="18" height="24" viewBox="0 0 18 24" aria-hidden="true" style="margin-top:2px"><path fill="#fff" d="M9 0a9 9 0 0 0-9 9c0 6.5 9 15 9 15s9-8.5 9-15a9 9 0 0 0-9-9zm0 12.5A3.5 3.5 0 1 1 9 5.5a3.5 3.5 0 0 1 0 7z"/></svg>
      <span>48 Meadowbrook Lane, Suite 200<br>Vaughan, ON L4K 2B3</span>
    </div>
    <span class="band-divider" style="left:519px"></span>
    <div class="band-contact">
      <div class="phone">
        <svg width="20" height="20" viewBox="0 0 24 24" aria-hidden="true"><path fill="#fff" d="M6.6 10.8a15.1 15.1 0 0 0 6.6 6.6l2.2-2.2a1 1 0 0 1 1-.25 11.4 11.4 0 0 0 3.6.57 1 1 0 0 1 1 1V20a1 1 0 0 1-1 1A17 17 0 0 1 3 4a1 1 0 0 1 1-1h3.5a1 1 0 0 1 1 1c0 1.25.2 2.45.57 3.57a1 1 0 0 1-.25 1z"/></svg>
        (905) 555-0148
      </div>
      <div class="web">
        <svg width="17" height="17" viewBox="0 0 24 24" aria-hidden="true" fill="none"><circle cx="12" cy="12" r="10" fill="#fff"/><path stroke="#5fbf74" stroke-width="1.4" d="M2 12h20M12 2c3 3 3 17 0 20M12 2c-3 3-3 17 0 20M4 7h16M4 17h16"/></svg>
        brightleafdentistry.ca
      </div>
    </div>
  </div>
</section>

</body>
</html>
```